Brill Insurance Agency - Business Cards

Hello, I am needing new trendy business cards for our Insurance Agency now that I have a new Logo. I have attached our new logo with several color options along with a business card design that I like. I am leaning towards burgundy and blue colors. I have attached our current business card. I have also attached a headshot of our company president, Martin Vale, that you can use if you wish. Thank you so much in advance for all the wonderful designs!!!!

Target Market(s)

We want to look very professional to potential customers and we also want to look very professional so insurance companies will want to contract with us to sell their product.

Industry/Entity Type

Insurance

Contact Information for Business Card

Martin Vale
mvale@brillagency.com
Business: 555-213-4087
Fax: 555-213-7751
Cell: 555-390-2618
Toll Free: 888-555-0194
42 W Elm Rd Marlow, MO 64901
www.brillagency.net

Font styles to use
Serif
Sans Serif

Colors
0355a3
3277b5
f04a50
ec1f27

Requirements
Nice to have
• I love creativity. The more creative and balanced a business card design the more I will like it. I would like the card to be printed horizontally instead of vertically.
Should not have
• My project should not have the Allied Coverage Network logo. It is no longer used in the industry.

```html
<!DOCTYPE html>
<html lang="en">
<head>
<meta charset="utf-8">
<title>Brill Insurance Agency – Business Cards</title>
<link href="https://fonts.googleapis.com/css2?family=Arimo:wght@400;700&family=Lato:wght@700&display=swap" rel="stylesheet">
<style>
  :root{
    --backdrop:#d6d6d6;
    --card-white:#ffffff;
    --burgundy:#6b1030;
    --burgundy-deep:#4f0c24;
    --teal:#16b3a3;
    --label-blue:#3a86c8;
    --ink:#333333;
  }
  *{margin:0;padding:0;box-sizing:border-box}
  html,body{width:1200px;height:800px;overflow:hidden;background:var(--backdrop)}
  .card{position:absolute;top:283px;width:430px;height:239px;overflow:hidden}
  .card-front{left:110px;background:var(--card-white)}
  .card-back{left:638px;background:radial-gradient(ellipse at 40% 25%,#7a1538 0%,var(--burgundy) 45%,var(--burgundy-deep) 100%)}

  .agency-name{position:absolute;font-family:"Arimo",sans-serif;font-weight:700;color:var(--teal);line-height:1;white-space:nowrap}
  .card-front .agency-name{left:0;width:100%;top:52px;text-align:center;font-size:18px}
  .card-back .agency-name{left:0;width:100%;top:108px;text-align:center;font-size:26px}

  .holder{position:absolute;left:39px;top:118px;font-family:"Arimo",sans-serif}
  .holder-name{font-size:13px;font-weight:700;color:var(--label-blue)}
  .holder-title{font-size:8px;color:var(--teal);margin-top:1px}

  .divider{position:absolute;left:30px;top:161px;width:370px;height:1px;background:var(--teal)}

  .contacts{position:absolute;top:170px;font-family:"Arimo",sans-serif;font-size:7.5px;color:var(--ink)}
  .contacts .row{display:flex;align-items:flex-start;height:16px}
  .contacts .label{font-size:9.5px;font-weight:700;color:var(--label-blue);margin-right:6px;white-space:nowrap}
  .col-1{left:39px}.col-2{left:159px}.col-3{left:272px}
  .contacts .value{padding-top:1.5px;line-height:1.25;white-space:nowrap}

  .footer-band{position:absolute;left:0;bottom:0;width:100%;height:20px;background:var(--burgundy)}
  .site{position:absolute;right:32px;top:4px;font-family:"Lato",sans-serif;font-weight:700;font-size:10px;color:#fff;letter-spacing:.5px}
</style>
</head>
<body>

<section class="card card-front">
  <div class="agency-name">Brill Insurance Agency</div>

  <div class="holder">
    <div class="holder-name">Martin Vale</div>
    <div class="holder-title">President</div>
  </div>

  <div class="divider"></div>

  <div class="contacts col-1">
    <div class="row"><span class="label">Telephone:</span><span class="value">888-555-0194</span></div>
    <div class="row"><span class="label">Cellphone:</span><span class="value">555-390-2618</span></div>
  </div>
  <div class="contacts col-2">
    <div class="row"><span class="label">Fax:</span><span class="value">555-213-7751</span></div>
    <div class="row"><span class="label">Business:</span><span class="value">555-213-4087</span></div>
  </div>
  <div class="contacts col-3">
    <div class="row"><span class="label">E-mail:</span><span class="value">mvale@brillagency.com</span></div>
    <div class="row"><span class="label">Address:</span><span class="value">42 W Elm Rd Marlow,<br>MO 64901</span></div>
  </div>

  <div class="footer-band"><span class="site">www.brillagency.net</span></div>
</section>

<section class="card card-back">
  <div class="agency-name">Brill Insurance Agency</div>
</section>

</body>
</html>
```